Business Card Design Project - Brantwell Media

We need a new business card that fits with our new logo. We are a social media agency and consultancy operating in China. We want a fresh and strong business card. Our cards need to be two-sided as we have both English and Chinese language names and addresses on the card, but as with our current business card this does not need to be a mirror-image. Our thoughts go out to a white card on the front where the logo/name is and then using the logo colours for different coloured back-grounds. i.e that the back of the biz card works with the four different colours in the logo.

Attached is the new logo, and also a copy of our old business cards.

Target Market(s)

CEO's, CMO's. media and advertising professionals

Industry/Entity Type

Business

Requirements
Must have
• inclusion of both Chinese and English language
Nice to have
• four different colored versions of the back of the biz card. Our logo has four colors and each of these colors we would like to have a version of.

```html
<!DOCTYPE html>
<html lang="en">
<head>
<meta charset="utf-8">
<title>Brantwell Media – Business Card Set</title>
<link rel="stylesheet" href="https://fonts.googleapis.com/css2?family=Arimo:wght@400;700&family=Noto+Sans+SC:wght@400;700&display=swap">
<style>
  :root {
    --paper: #ffffff;
    --ink: #111111;
    --ink-soft: #333333;
    --green: #8cc63f;
    --purple: #662d91;
    --magenta: #ec008c;
    --orange: #f26522;
    --shadow: 2px 3px 7px rgba(0, 0, 0, 0.35);
    --latin: "Arimo", Arial, sans-serif;
    --hanzi: "Noto Sans SC", "Arimo", sans-serif;
  }
  html, body {
    margin: 0;
    padding: 0;
    width: 1200px;
    height: 686px;
    overflow: hidden;
    background: var(--paper);
  }
  .sheet {
    position: relative;
    width: 1200px;
    height: 686px;
    font-family: var(--latin);
  }
  .card {
    position: absolute;
    width: 249px;
    height: 153px;
    box-shadow: var(--shadow);
    overflow: hidden;
  }
  .theme-green  { --accent: var(--green); }
  .theme-purple { --accent: var(--purple); }
  .theme-magenta{ --accent: var(--magenta); }
  .theme-orange { --accent: var(--orange); }

  .card--front { background: var(--paper); color: var(--ink); }
  .card--back  { background: var(--accent); color: var(--paper); }

  .wordmark {
    position: absolute;
    top: 22px;
    right: 13px;
    display: flex;
    align-items: center;
    gap: 5px;
    font-family: var(--latin);
    font-weight: 700;
    font-size: 18px;
    letter-spacing: -0.3px;
    line-height: 1;
    white-space: nowrap;
  }
  .wordmark__dot {
    width: 7px;
    height: 7px;
    background: var(--accent);
  }
  .card--back .wordmark__dot { background: var(--paper); }

  .holder {
    position: absolute;
    left: 14px;
    bottom: 13px;
  }
  .holder__name {
    font-size: 17px;
    font-weight: 400;
    letter-spacing: -0.2px;
    line-height: 1;
    white-space: nowrap;
  }
  .holder__role {
    font-size: 7.5px;
    color: var(--ink-soft);
    margin-top: 1px;
  }

  .contact {
    position: absolute;
    left: 152px;
    bottom: 13px;
    margin: 0;
    display: grid;
    grid-template-columns: auto auto;
    column-gap: 4px;
    row-gap: 0;
    font-size: 5.6px;
    line-height: 7px;
    white-space: nowrap;
  }
  .contact dt { font-weight: 700; color: var(--accent); text-align: right; }
  .contact dd { margin: 0; color: var(--ink); }

  .cn-holder {
    position: absolute;
    left: 14px;
    top: 88px;
    display: flex;
    align-items: baseline;
    gap: 6px;
    font-family: var(--hanzi);
  }
  .cn-holder__name { font-size: 14px; font-weight: 700; }
  .cn-holder__role { font-size: 7px; }

  .address {
    position: absolute;
    left: 14px;
    width: 150px;
    font-size: 5.2px;
    line-height: 6.6px;
    white-space: nowrap;
  }
  .address--cn { top: 109px; font-family: var(--hanzi); }
  .address--en { top: 126px; font-weight: 700; }

  .website {
    position: absolute;
    right: 13px;
    bottom: 13px;
    font-size: 6.8px;
    line-height: 7px;
    white-space: nowrap;
  }
</style>
</head>
<body>
<main class="sheet">

  <section class="card card--front theme-green" style="left:27px; top:144px;">
    <div class="wordmark"><span class="wordmark__dot"></span>Brantwell Media</div>
    <div class="holder">
      <div class="holder__name">Daniel Hartley</div>
      <div class="holder__role">managing director</div>
    </div>
    <dl class="contact">
      <dt>email:</dt><dd>dan@brantwellchina.com</dd>
      <dt>chat:</dt><dd>danhartley.bj</dd>
      <dt>mobile:</dt><dd>+86 13800245817</dd>
    </dl>
  </section>
  <section class="card card--back theme-green" style="left:304px; top:144px;">
    <div class="wordmark"><span class="wordmark__dot"></span>Brantwell Media</div>
    <div class="cn-holder"><span class="cn-holder__name">韩德礼</span><span class="cn-holder__role">董事总经理</span></div>
    <div class="address address--cn">东直门外大街鸿源商务中心C310 东直门外大街鸿源中心C310<br>东城区东直门外大街鸿源商务中心 北京 (100027)</div>
    <div class="address address--en">Suite C310, Hong Yuan Commercial Centre<br>Dongzhimen Outer St Dongcheng, Beijing 100027</div>
    <div class="website">www.brantwellchina.com</div>
  </section>

  <section class="card card--front theme-purple" style="left:647px; top:144px;">
    <div class="wordmark"><span class="wordmark__dot"></span>Brantwell Media</div>
    <div class="holder">
      <div class="holder__name">Daniel Hartley</div>
      <div class="holder__role">managing director</div>
    </div>
    <dl class="contact">
      <dt>email:</dt><dd>dan@brantwellchina.com</dd>
      <dt>chat:</dt><dd>danhartley.bj</dd>
      <dt>mobile:</dt><dd>+86 13800245817</dd>
    </dl>
  </section>
  <section class="card card--back theme-purple" style="left:923px; top:144px;">
    <div class="wordmark"><span class="wordmark__dot"></span>Brantwell Media</div>
    <div class="cn-holder"><span class="cn-holder__name">韩德礼</span><span class="cn-holder__role">董事总经理</span></div>
    <div class="address address--cn">东直门外大街鸿源商务中心C310 东直门外大街鸿源中心C310<br>东城区东直门外大街鸿源商务中心 北京 (100027)</div>
    <div class="address address--en">Suite C310, Hong Yuan Commercial Centre<br>Dongzhimen Outer St Dongcheng, Beijing 100027</div>
    <div class="website">www.brantwellchina.com</div>
  </section>

  <section class="card card--front theme-magenta" style="left:27px; top:387px;">
    <div class="wordmark"><span class="wordmark__dot"></span>Brantwell Media</div>
    <div class="holder">
      <div class="holder__name">Daniel Hartley</div>
      <div class="holder__role">managing director</div>
    </div>
    <dl class="contact">
      <dt>email:</dt><dd>dan@brantwellchina.com</dd>
      <dt>chat:</dt><dd>danhartley.bj</dd>
      <dt>mobile:</dt><dd>+86 13800245817</dd>
    </dl>
  </section>
  <section class="card card--back theme-magenta" style="left:304px; top:387px;">
    <div class="wordmark"><span class="wordmark__dot"></span>Brantwell Media</div>
    <div class="cn-holder"><span class="cn-holder__name">韩德礼</span><span class="cn-holder__role">董事总经理</span></div>
    <div class="address address--cn">东直门外大街鸿源商务中心C310 东直门外大街鸿源中心C310<br>东城区东直门外大街鸿源商务中心 北京 (100027)</div>
    <div class="address address--en">Suite C310, Hong Yuan Commercial Centre<br>Dongzhimen Outer St Dongcheng, Beijing 100027</div>
    <div class="website">www.brantwellchina.com</div>
  </section>

  <section class="card card--front theme-orange" style="left:647px; top:387px;">
    <div class="wordmark"><span class="wordmark__dot"></span>Brantwell Media</div>
    <div class="holder">
      <div class="holder__name">Daniel Hartley</div>
      <div class="holder__role">managing director</div>
    </div>
    <dl class="contact">
      <dt>email:</dt><dd>dan@brantwellchina.com</dd>
      <dt>chat:</dt><dd>danhartley.bj</dd>
      <dt>mobile:</dt><dd>+86 13800245817</dd>
    </dl>
  </section>
  <section class="card card--back theme-orange" style="left:923px; top:387px;">
    <div class="wordmark"><span class="wordmark__dot"></span>Brantwell Media</div>
    <div class="cn-holder"><span class="cn-holder__name">韩德礼</span><span class="cn-holder__role">董事总经理</span></div>
    <div class="address address--cn">东直门外大街鸿源商务中心C310 东直门外大街鸿源中心C310<br>东城区东直门外大街鸿源商务中心 北京 (100027)</div>
    <div class="address address--en">Suite C310, Hong Yuan Commercial Centre<br>Dongzhimen Outer St Dongcheng, Beijing 100027</div>
    <div class="website">www.brantwellchina.com</div>
  </section>

</main>
</body>
</html>
```